Marlowick community hall home page

We are building a modern, responsive website & booking system for our community hall. For this PixelForge task, we would like to receive design ideas for the home page.
There are no limits on the colours or fonts that can be used. We are looking for a modern, fresh design with a local/community feel. We don’t have a logo but we also recognise that our name is quite long! … So initials (MCH) instead of the name would be fine.
People book our community hall for a range of activities including: fitness classes, wedding receptions, birthday parties, business meetings, teaching, community events, charity fundraisers and other celebrations.
We have three main goals for the website. The first is that people can check our calendar and make a booking for an available time slot. The second is that they can read about our facilities and the prices for hiring them. The third is that people can find out about upcoming activities & events.
CTA: Book now
A button that links to a booking request form. (The form is not part of this design project)
Primary/Header navigation:
Home | Calendar | Facilities | Prices | Photos | News | Contact
Secondary/Footer navigation:
Chatterleaf | Quillcast
Login | Register | Privacy policy | Terms & conditions
Example texts (lorem ipsum etc. is also fine):
We have everything you need from a venue, whether it’s an elegant room with ample flexible space, a lavish and elegant hall for a wedding reception, a conference room that fits 125 delegates or a easy access venue to the town centre.
The hall is available for hire for wedding receptions, birthday celebrations, anniversaries, children's parties, presentations, lectures, fitness groups, and will comfortably accommodate all your guests.
This venue is well equipped with a modern kitchen, a range of audio and technical services, hearing loop, licensed bar, conference facilities, disabled access and unlimited free WiFi.
You can use this website to find out more about our rooms, equipment and the services we can offer and use the calendar to see where we have rooms available. You can also book rooms using our online booking system.
To the front of the building is a large public open grassed area across which is a row of shops. To the rear of the building is the large car park, including spaces for blue badge holders and a large enclosed cycle rack. This area also has extensive gardens, with seating and planting areas maintained by local volunteers.
The community hall is run and managed by volunteers of the Marlowick Community Organisation. Our objectives are to increase opportunities for people living in and around Pepperton.
We are passionate about being the heart of the community; caring for this community centred property and visitors are at the heart of all we do.
Where to go next
— Check when the hall is free
— Read our booking policy documents
— Make a booking reservation
Amenities
— Free WiFi
— Free car parking
— Fully equipped kitchen
— Hearing loop
Details for our most popular facilities (rooms):
Name: Main hall
Short description: A 127 square metre main hall with entrance lobby, toilets, a well-equipped kitchen and separate storage facilities. Three sets of double doors provide access to a large paved area and the adjacent playing field.
Capacity: 180 people
Price: £10-20 per hour
Links: More info | Book now
Name: Large meeting room
Short description: A delightful, spacious room with an outlook and access to the small walled garden. Ideal for meetings and small gatherings - it has its own access door and the use of a disabled W/C. We offer a reduced rate for this room when booked together with the main hall.
Capacity: 20 people
Price: £6-12 per hour
Attachments:
We have attached some photos of the hall & some (royalty free) stock images for inspiration.

```html
<!DOCTYPE html>
<html lang="en">
<head>
<meta charset="utf-8">
<title>Marlowick Community Hall</title>
<link href="https://fonts.googleapis.com/css2?family=Marcellus&family=Montserrat:wght@400;500&family=Arimo:wght@400;700&family=Tinos&display=swap" rel="stylesheet">
<style>
:root{
  --red:#c41a06;
  --red-bright:#ee1c0a;
  --red-dark:#9b1404;
  --ink:#1a1a1a;
  --text:#2b2b2b;
  --panel:#f4f4f4;
  --tile:#e9ebee;
  --tile-line:#c9ccd1;
  --white:#fff;
}
*{box-sizing:border-box;margin:0;padding:0}
html,body{width:1200px;height:4200px;overflow:hidden;background:var(--white)}
body{position:relative;font-family:"Montserrat",sans-serif;color:var(--text)}
.abs{position:absolute}

/* header */
.site-header{left:0;top:0;width:1200px;height:88px;background:rgba(236,236,236,.93);z-index:2}
.brand{left:152px;top:18px;font-family:"Arimo",sans-serif;color:var(--ink);line-height:1}
.brand-name{font-size:28px;font-weight:700;letter-spacing:.5px}
.brand-sub{font-size:19px;letter-spacing:1px;margin-top:2px}
.main-nav{left:436px;top:36px;display:flex;gap:22px;font-family:"Arimo",sans-serif;font-size:14px;color:var(--ink)}
.main-nav .current{color:var(--red-bright);text-decoration:underline}
.login-btn{left:985px;top:33px;width:62px;height:26px;background:var(--red-bright);color:#fff;font-family:"Arimo",sans-serif;font-size:13px;text-align:center;line-height:26px}

/* hero */
.hero-photo{left:0;top:88px;width:1200px;height:435px;background:linear-gradient(100deg,#3b2a4d 0%,#7a4aa8 30%,#5e3a52 55%,#a4536a 75%,#3c2a33 100%)}
.hero-title{left:155px;top:262px;font-family:"Tinos",serif;font-size:37px;line-height:45px;color:#fff}
.btn-red{background:var(--red-bright);color:#fff;font-family:"Arimo",sans-serif;text-align:center}
.hero-know{left:155px;top:430px;width:152px;height:33px;line-height:33px;font-size:17px}
.hero-book{left:338px;top:430px;width:130px;height:33px;line-height:33px;font-size:17px}

/* intro */
.intro{left:180px;top:595px;width:860px;font-size:17px;line-height:27px;color:var(--ink)}
.intro p+p{margin-top:27px}

.section-title{width:1200px;left:0;text-align:center;font-family:"Marcellus",serif;font-size:36px;letter-spacing:1px;color:var(--ink)}
.amenities-lead{left:170px;top:908px;width:860px;text-align:center;font-size:17px;line-height:27px;color:var(--ink)}

.amenity{width:180px;height:231px;top:1024px;background:var(--tile);border:2px solid var(--tile-line);text-align:center}
.amenity svg{margin-top:28px}
.amenity-label{font-family:"Arimo",sans-serif;font-weight:700;font-size:17px;line-height:22px;color:var(--ink);margin-top:10px}

/* facilities */
.facility-photo{role:img}
.facility-card{background:var(--red);color:#fff;padding:44px 44px}
.facility-card h3{font-family:"Marcellus",serif;font-weight:400;font-size:22px;letter-spacing:1px;margin-bottom:22px}
.facility-card p{font-size:12.5px;line-height:17px;margin-bottom:18px}
.facility-links{display:flex;gap:26px;margin-top:8px}
.facility-links span{background:#fff;color:var(--ink);font-family:"Arimo",sans-serif;font-size:13px;padding:4px 12px}

/* gallery */
.gallery-tile{}
.view-more{left:478px;top:3156px;width:223px;height:41px;line-height:41px;font-size:18px}

/* next steps */
.next-steps{left:0;top:3283px;width:1200px;height:466px;background:var(--panel)}
.next-label{top:3362px;width:260px;text-align:center;font-family:"Montserrat",sans-serif;font-size:27px;line-height:36px;color:var(--ink)}
.next-label.link{color:var(--red)}

/* footer */
.site-footer{left:0;top:3749px;width:1200px;height:360px;background:var(--red);color:#fff}
.footer-brand{left:150px;top:3806px;font-family:"Arimo",sans-serif;line-height:1}
.footer-brand .brand-name{font-size:40px;letter-spacing:1px}
.footer-brand .brand-sub{font-size:28px;letter-spacing:1.5px;margin-top:2px}
.footer-legal{left:150px;top:3898px;font-size:13px;line-height:18px}
.footer-links{left:150px;top:3952px;font-size:13px;line-height:36px}
.footer-nav{left:599px;top:3806px;font-size:13px;line-height:36px}
.social-bar{left:0;top:4109px;width:1200px;height:91px;background:var(--red-dark);display:flex;justify-content:center;align-items:center;gap:44px;color:#fff;font-family:"Arimo",sans-serif;font-size:17px}
.social{display:flex;align-items:center;gap:10px}
.social i{display:block;width:30px;height:30px;background:#fff}
</style>
</head>
<body>

<header class="abs site-header">
  <div class="abs brand"><div class="brand-name">MARLOWICK</div><div class="brand-sub">COMMUNITY HALL</div></div>
  <nav class="abs main-nav">
    <span class="current">HOME</span><span>CALENDAR</span><span>FACILITIES</span><span>PRICES</span><span>PHOTOS</span><span>NEWS</span><span>CONTACT</span>
  </nav>
  <div class="abs login-btn">LOGIN</div>
</header>

<div class="abs hero-photo" role="img" aria-label="Guests seated at round tables in the hall under purple lighting and stained glass windows"></div>
<h1 class="abs hero-title" style="font-weight:400">We Have Everything<br>You Need<br>From a Venue</h1>
<div class="abs btn-red hero-know">KNOW MORE</div>
<div class="abs btn-red hero-book">BOOK NOW</div>

<section class="abs intro">
  <p>We have everything you need from a venue, whether it’s an elegant room with ample flexible space, a lavish and elegant hall for a wedding reception, a conference room that fits 125 delegates or a easy access venue to the town centre.</p>
  <p>The hall is available for hire for wedding receptions, birthday celebrations, anniversaries, children's parties, presentations, lectures, fitness groups, and will comfortably accommodate all your guests.</p>
</section>

<h2 class="abs section-title" style="top:815px">AMENITIES</h2>
<p class="abs amenities-lead">We are passionate about being the heart of the community; caring for this community centred property and visitors are at the heart of all we do.&nbsp; This venue is equipped with all the necessary equipment and amenities to make your stay enjoyable.</p>

<div class="abs amenity" style="left:171px">
  <svg width="120" height="90" viewBox="0 0 120 90"><g fill="none" stroke="#b5160a" stroke-width="10" stroke-linecap="round"><path d="M15 35a64 64 0 0 1 90 0"/><path d="M32 52a40 40 0 0 1 56 0"/></g><circle cx="60" cy="72" r="9" fill="#b5160a"/></svg>
  <div class="amenity-label">FREE WI-FI</div>
</div>
<div class="abs amenity" style="left:396px">
  <svg width="140" height="90" viewBox="0 0 140 90"><path d="M22 40l10-22h50l10 22h6v30H16V40z" fill="#b5160a"/><rect x="38" y="24" width="38" height="14" fill="#e9ebee"/><circle cx="30" cy="56" r="6" fill="#e9ebee"/><circle cx="84" cy="56" r="6" fill="#e9ebee"/><rect x="20" y="70" width="14" height="12" fill="#b5160a"/><rect x="80" y="70" width="14" height="12" fill="#b5160a"/><rect x="104" y="2" width="30" height="34" fill="#b5160a"/><text x="119" y="29" fill="#fff" font-family="Arimo" font-weight="700" font-size="26" text-anchor="middle">P</text><rect x="116" y="36" width="6" height="50" fill="#b5160a"/></svg>
  <div class="amenity-label">FREE CAR<br>PARKING</div>
</div>
<div class="abs amenity" style="left:621px">
  <svg width="120" height="90" viewBox="0 0 120 90"><path d="M60 4L6 46h14v40h80V46h14z" fill="#b5160a"/><g fill="#e9ebee"><rect x="38" y="38" width="4" height="44"/><rect x="32" y="38" width="3" height="16"/><rect x="45" y="38" width="3" height="16"/><path d="M58 38h6v44h-6z"/><path d="M76 38c10 0 10 24 2 26v18h-4V38z"/></g></svg>
  <div class="amenity-label">FULLY-EQUIPPED<br>KITCHEN</div>
</div>
<div class="abs amenity" style="left:848px">
  <svg width="120" height="90" viewBox="0 0 120 90"><path d="M50 36a22 22 0 1 1 40 12c-6 8-12 10-14 22-2 10-14 14-22 8" fill="none" stroke="#b5160a" stroke-width="10" stroke-linecap="round"/><path d="M62 40a8 8 0 1 1 14 6" fill="none" stroke="#b5160a" stroke-width="7" stroke-linecap="round"/><path d="M26 84l70-70" stroke="#b5160a" stroke-width="8"/></svg>
  <div class="amenity-label">HEARING LOOP</div>
</div>

<h2 class="abs section-title" style="left:-20px;top:1345px">MOST POPULAR FACILITIES</h2>

<div class="abs" style="left:29px;top:1447px;width:564px;height:375px;background:radial-gradient(circle at 45% 60%,#e07a2a 0%,#8e3a8c 35%,#4a2468 75%,#2c1a3e 100%)" role="img" aria-label="Candle lantern centrepiece on a table in the purple-lit main hall"></div>
<article class="abs facility-card" style="left:570px;top:1477px;width:594px;height:316px">
  <h3>MAIN HALL</h3>
  <p>A 127 square metre main hall with entrance lobby, toilets, a well-equipped kitchen and separate storage facilities. Three sets of double doors provide access to a large paved area and the adjacent playing field.</p>
  <p>Capacity: 180 people</p>
  <p>Price: £10-20 per hour</p>
  <div class="facility-links"><span>MORE INFO</span><span>BOOK NOW</span></div>
</article>

<div class="abs" style="left:597px;top:1824px;width:567px;height:404px;background:linear-gradient(180deg,#c9cdd6 0%,#e6e4e0 45%,#8a7560 75%,#2f3d5a 100%)" role="img" aria-label="Large meeting room with a long table set for a meeting and a projector screen"></div>
<article class="abs facility-card" style="left:29px;top:1857px;width:595px;height:339px">
  <h3>LARGE MEETING ROOM</h3>
  <p>A delightful, spacious room with an outlook and access to the small walled garden. Ideal for meetings and small gatherings - it has its own access door and the use of a disabled W/C. We offer a reduced rate for this room when booked together with the main hall.</p>
  <p>Capacity: 20 people</p>
  <p>Price: £6-12 per hour</p>
  <div class="facility-links"><span>MORE INFO</span><span>BOOK NOW</span></div>
</article>

<h2 class="abs section-title" style="top:2343px">GALLERY</h2>
<div class="abs" style="left:18px;top:2439px;width:259px;height:295px;background:linear-gradient(135deg,#3f5a36,#b83040 50%,#e8e4e0)" role="img" aria-label="Flowers and crystal glasses on a table"></div>
<div class="abs" style="left:285px;top:2439px;width:435px;height:295px;background:linear-gradient(135deg,#2a6a78,#e8a0b0 50%,#4fa0a8)" role="img" aria-label="Party cake stand with pastel treats"></div>
<div class="abs" style="left:730px;top:2439px;width:453px;height:295px;background:linear-gradient(160deg,#d8b82a,#e8d890 50%,#b09020)" role="img" aria-label="Children jumping on a bouncy castle"></div>
<div class="abs" style="left:18px;top:2747px;width:533px;height:366px;background:linear-gradient(180deg,#1e4a7a,#2a8aa8 45%,#1a1a28)" role="img" aria-label="Crowd dancing at a party with confetti and lights"></div>
<div class="abs" style="left:561px;top:2747px;width:622px;height:366px;background:linear-gradient(135deg,#6a5040,#d8d0c8 50%,#8a7868)" role="img" aria-label="Candles and glassware on a wedding table"></div>
<div class="abs btn-red view-more">VIEW MORE PHOTOS</div>

<section class="abs next-steps"></section>
<div class="abs next-label" style="left:163px">Check out when<br>the hall is free.</div>
<div class="abs next-label link" style="left:471px">Read our booking<br>policy documents</div>
<div class="abs next-label" style="left:768px">Make a booking<br>reservation</div>

<svg class="abs" style="left:211px;top:3485px" width="152" height="176" viewBox="0 0 152 176"><rect x="6" y="20" width="140" height="150" rx="14" fill="none" stroke="#c41a06" stroke-width="10"/><rect x="6" y="20" width="140" height="36" fill="#c41a06"/><g fill="#c41a06"><rect x="30" y="4" width="12" height="34" rx="6"/><rect x="58" y="4" width="12" height="34" rx="6"/><rect x="84" y="4" width="12" height="34" rx="6"/><rect x="110" y="4" width="12" height="34" rx="6"/><rect x="24" y="72" width="22" height="18"/><rect x="54" y="72" width="22" height="18"/><rect x="84" y="72" width="22" height="18"/><rect x="114" y="72" width="16" height="18"/><rect x="24" y="98" width="22" height="18"/><rect x="54" y="98" width="22" height="18"/><rect x="84" y="98" width="22" height="18"/><rect x="114" y="98" width="16" height="18"/><rect x="24" y="124" width="22" height="18"/><rect x="54" y="124" width="22" height="18"/><rect x="84" y="124" width="22" height="18"/><rect x="114" y="124" width="16" height="18"/></g></svg>

<svg class="abs" style="left:523px;top:3485px" width="170" height="176" viewBox="0 0 170 176"><path d="M26 6h130v150a14 14 0 0 1-14 14H18a14 14 0 0 1-14-14v-16h22z" fill="none" stroke="#c41a06" stroke-width="8" stroke-linejoin="round"/><path d="M4 140h112v16a14 14 0 0 0 14 14" fill="none" stroke="#c41a06" stroke-width="8"/><path d="M80 24l22 8v14c0 14-10 22-22 26-12-4-22-12-22-26V32z" fill="none" stroke="#c41a06" stroke-width="6"/><path d="M70 46l8 8 14-14" fill="none" stroke="#c41a06" stroke-width="6"/><g stroke="#c41a06" stroke-width="6"><path d="M44 88h90M44 104h90M44 120h90"/></g></svg>

<svg class="abs" style="left:800px;top:3485px" width="210" height="218" viewBox="0 0 210 218"><rect x="6" y="20" width="160" height="150" rx="14" fill="none" stroke="#c41a06" stroke-width="10"/><rect x="6" y="20" width="160" height="40" fill="#c41a06"/><g fill="#c41a06"><rect x="36" y="4" width="14" height="36" rx="7"/><rect x="122" y="4" width="14" height="36" rx="7"/><rect x="24" y="78" width="26" height="22"/><rect x="60" y="78" width="26" height="22"/><rect x="96" y="78" width="26" height="22"/><rect x="24" y="110" width="26" height="22"/><rect x="60" y="110" width="26" height="22"/><rect x="24" y="142" width="26" height="20"/></g><circle cx="155" cy="160" r="50" fill="#f4f4f4" stroke="#c41a06" stroke-width="10"/><path d="M130 160l18 18 30-32" fill="none" stroke="#c41a06" stroke-width="11" stroke-linecap="round" stroke-linejoin="round"/></svg>

<footer class="abs site-footer"></footer>
<div class="abs footer-brand" style="color:#fff"><div class="brand-name">MARLOWICK</div><div class="brand-sub">COMMUNITY HALL</div></div>
<div class="abs footer-legal" style="color:#fff">Copyright 2021 Marlowick Community Hall<br>All Rights Reserved</div>
<div class="abs footer-links" style="color:#fff">Privacy Policy<br>Terms and Conditions<br>Login<br>Register</div>
<nav class="abs footer-nav" style="color:#fff">Home<br>Calendar<br>Facilities<br>Prices<br>Photos<br>News<br>Contact</nav>
<div class="abs social-bar">
  <span class="social"><i></i>Chatterleaf</span>
  <span class="social"><i></i>Quillcast</span>
</div>

</body>
</html>
```